Tax Firm - Creative Print Ads to Build New Clients

I'm the marketing director of an integrated financial services business based in Melbourne Australia. I need to create a series of 4 press ads to run in the local business newspaper.

Each ad needs to stand alone, but at the same time should appear visually as from the same company and be part of a series.

The ad will will 115mm by 255mm (1/3 of a page horizontal)

Final artwork needs to be setup using CMYK and at the exact dimensions no bleed.

Brief
- Our tax practice provides services to individuals & small businesses (cafes, tradespeoeple, retailers)
- Our tagline is Bold, Proactive, Strategic, Practical financial advice, Where Futures Settle (a brand logo will be provided)
- The company logo needs to be included
- Web address included
- phone number included
- The ad needs to be professional, yet energetic
- Stock photography should be at an absolute minimum where models are not identifable
- Graphics are prefered over stock images
- Sketches are great
- Key message - we do tax returns, we care about you as an individual, we've been in the Docklands for 20 years, we are your local partner in your financial journey
Updates

Target Market(s)

Individuals earning between 50,000 and 200,000 per annum

Industry/Entity Type

Accounting

Font styles to use
Sans Serif
Script

Colors
3176b5
1b1b1b
fbf289
ec1f27
85acd3
0355a3

Requirements
Must have
• Sell t services to individuals as primary audience, with small businesses as a secondary audience.
• ---- Updated ----
• The company is www.velmorbay.com.au
• I've added
• - logos (vertical, horizontal, reverse and our brand tagline too)
• - Brand Guidelines
Nice to have
• I want to see some graphics that sell the idea that we are a local firm with 20 years experience in the area.
• We care about individuals first
Should not have
• Avoid using stock images where the pretty model is identifiable, we hate to see actors in our ads

```html
<!DOCTYPE html>
<html lang="en">
<head>
<meta charset="utf-8">
<title>Velmor Bay – Press Ad Series</title>
<link href="https://fonts.googleapis.com/css2?family=Ubuntu:wght@400;500;700&family=Allura&display=swap" rel="stylesheet">
<style>
  :root{
    --stage:#647591;
    --paper:#ffffff;
    --band:#0d0d0d;
    --headline:#5b84c8;
    --body:#6f6f6f;
    --band-text:#f2f2f2;
    --shadow:rgba(20,28,45,.45);
  }
  *{margin:0;padding:0;box-sizing:border-box}
  html,body{width:1200px;height:800px;overflow:hidden}
  body{background:var(--stage);position:relative;font-family:"Ubuntu",sans-serif}

  .ad{position:absolute;width:568px;height:256px;background:var(--paper);box-shadow:0 4px 10px var(--shadow);overflow:hidden}
  .ad--tape{left:24px;top:126px}
  .ad--cube{left:604px;top:126px}
  .ad--glass{left:24px;top:393px}
  .ad--key{left:604px;top:393px}

  .headline{position:absolute;text-align:center;color:var(--headline);font-size:21.5px;line-height:24px;font-weight:400;text-transform:uppercase;letter-spacing:.2px}
  .headline strong{font-weight:700}
  .body-copy{position:absolute;text-align:center;color:var(--body);font-size:7.3px;line-height:10px}

  .visual{position:absolute}

  .band{position:absolute;left:0;bottom:0;width:100%;height:56px;background:var(--band);color:var(--band-text)}
  .brand{position:absolute;left:28px;top:12px;display:flex;align-items:center;gap:8px}
  .brand-mark{width:24px;height:24px;border:1.5px solid var(--band-text);border-radius:50%}
  .brand-name{font-size:16px;letter-spacing:3.4px;font-weight:400;line-height:16px}
  .brand-url{position:absolute;left:66px;top:33px;font-size:7px;letter-spacing:.3px}
  .values{position:absolute;right:40px;top:16px;font-size:8.5px;letter-spacing:1.6px;font-weight:500;word-spacing:4px}
  .tagline{position:absolute;right:18px;top:28px;font-family:"Allura",cursive;font-size:12px}
</style>
</head>
<body>

<section class="ad ad--tape">
  <h2 class="headline" style="left:14px;top:45px;width:280px"><strong>A good track record<br>goes a long way.</strong><br>We know, we've<br>measured it.</h2>
  <p class="body-copy" style="left:14px;top:166px;width:280px">We're a team of Accountants with deep tax planning, tax management,<br>tax compliance and tax minimisation experience.</p>
  <div class="visual" role="img" aria-label="Coiled yellow measuring tape" style="left:306px;top:52px;width:226px;height:102px;border-radius:50px;background:radial-gradient(ellipse at 55% 50%,#f3d23a 0%,#e6be2a 55%,rgba(255,255,255,0) 75%)"></div>
  <div class="band">
    <div class="brand"><span class="brand-mark"></span><span class="brand-name">VELMOR BAY</span></div>
    <span class="brand-url">www.velmorbay.com.au</span>
    <span class="values">BOLD PROACTIVE STRATEGIC PRACTICAL</span>
    <span class="tagline">Where Futures Settle</span>
  </div>
</section>

<section class="ad ad--cube">
  <h2 class="headline" style="left:23px;top:41px;width:280px"><strong>We build client<br>relationships</strong><br>on a foundation of<br>trust and integrity.</h2>
  <p class="body-copy" style="left:23px;top:166px;width:280px">Our Property Insights Team brings decades of experience to your<br>professional property transactions.</p>
  <div class="visual" role="img" aria-label="Twisted colourful puzzle cube" style="left:360px;top:32px;width:140px;height:144px;border-radius:14px;background:linear-gradient(135deg,#e8473b 0%,#f2d43a 35%,#3a6cc4 65%,#eeeeee 100%)"></div>
  <div class="band">
    <div class="brand"><span class="brand-mark"></span><span class="brand-name">VELMOR BAY</span></div>
    <span class="brand-url">www.velmorbay.com.au</span>
    <span class="values">BOLD PROACTIVE STRATEGIC PRACTICAL</span>
    <span class="tagline">Where Futures Settle</span>
  </div>
</section>

<section class="ad ad--glass">
  <h2 class="headline" style="left:16px;top:60px;width:280px"><strong>Think ahead.</strong><br>Given more time,<br>imagine the prospects.</h2>
  <p class="body-copy" style="left:16px;top:170px;width:280px">Every person with financial goals will benefit from speaking to a<br>specialist before making financial decisions.</p>
  <div class="visual" role="img" aria-label="Hourglass with dark sand" style="left:392px;top:19px;width:76px;height:170px;border-radius:30px;background:linear-gradient(180deg,#d9d9d9 0%,#2a2a2a 25%,#f2f2f2 50%,#e8e8e8 75%,#1e1e1e 100%)"></div>
  <div class="band">
    <div class="brand"><span class="brand-mark"></span><span class="brand-name">VELMOR BAY</span></div>
    <span class="brand-url">www.velmorbay.com.au</span>
    <span class="values">BOLD PROACTIVE STRATEGIC PRACTICAL</span>
    <span class="tagline">Where Futures Settle</span>
  </div>
</section>

<section class="ad ad--key">
  <h2 class="headline" style="left:10px;top:55px;width:280px"><strong>Opening doors.</strong><br>Advice beyond<br>investment.</h2>
  <p class="body-copy" style="left:10px;top:160px;width:290px">Establishing a clear strategy and plan of action before you set off on your<br>investment journey is the key to reaching your investment and retirement<br>goals through property.</p>
  <div class="visual" role="img" aria-label="Antique brass key" style="left:310px;top:44px;width:200px;height:120px;border-radius:60px;background:radial-gradient(ellipse at 60% 50%,#c9a24e 0%,#a9822f 45%,rgba(255,255,255,0) 72%)"></div>
  <div class="band">
    <div class="brand"><span class="brand-mark"></span><span class="brand-name">VELMOR BAY</span></div>
    <span class="brand-url">www.velmorbay.com.au</span>
    <span class="values">BOLD PROACTIVE STRATEGIC PRACTICAL</span>
    <span class="tagline">Where Futures Settle</span>
  </div>
</section>

</body>
</html>
```